Business Card for new Architectural Firm

I intend to practice in a rural mountain community in upstate NY, focusing on residential and light commercial projects, including second home / vacation properties. I wish to convey a feeling of rural outdoorsy modernity.

Color is important - bold and urbane. Secondary or tertiary colors preferred.

Font is important, idiosyncratic is ok

Optionally, I may choose to use the name Brackenfold Studio. If used as part of your design, all of the Must Haves are still required.

Images uploaded are logos I like

Industry/Entity Type

Residential

Contact Information for Business Card

Lionel Harwicke
Architect (This word should stand alone or be associated with my name - not license number)
NY License No. 052816
lionel@designlhq.com
607 382 9154

Font styles to use
Sans Serif
Decorative

Requirements
Must have
• Whatever files I need to best utilize your design
• PDF
• JPG
• EPS
• Vectorwhatsit
Nice to have
• Logo or element that can be incorporated into other print material.
• Could be a font based card
Should not have
• no clip art
• No templates
• no floor plans
• no building photographs

```html
<!DOCTYPE html>
<html lang="en">
<head>
<meta charset="utf-8">
<title>Brackenfold Studio — Business Card</title>
<link href="https://fonts.googleapis.com/css2?family=Righteous&family=Didact+Gothic&display=swap" rel="stylesheet">
<style>
  :root {
    --page: #ffffff;
    --leaf-base: #72e000;
    --leaf-light: #84ee1c;
    --leaf-dark: #5cc800;
    --name-yellow: #ffd200;
    --name-shadow: rgba(70, 110, 0, 0.55);
    --ink: #2f3a12;
    --studio-green: #b2f548;
    --studio-edge: rgba(60, 130, 0, 0.7);
    --rule-red: #e8432a;
  }
  * { margin: 0; padding: 0; box-sizing: border-box; }
  html, body {
    width: 1200px;
    height: 838px;
    overflow: hidden;
    background: var(--page);
  }
  .card {
    position: absolute;
    left: 186px;
    top: 185px;
    width: 830px;
    height: 461px;
    overflow: hidden;
  }
  .card__foliage {
    position: absolute;
    inset: 0;
    background:
      radial-gradient(ellipse at 30% 30%, var(--leaf-light) 0%, transparent 55%),
      radial-gradient(ellipse at 75% 70%, var(--leaf-dark) 0%, transparent 60%),
      linear-gradient(160deg, var(--leaf-light), var(--leaf-base) 50%, var(--leaf-dark));
  }
  .card__name {
    position: absolute;
    left: 90px;
    top: 118px;
    font-family: "Righteous", sans-serif;
    font-weight: 400;
    font-size: 52px;
    letter-spacing: 1px;
    color: var(--name-yellow);
    text-shadow: 3px 3px 3px var(--name-shadow);
    white-space: nowrap;
  }
  .card__title {
    position: absolute;
    left: 91px;
    top: 186px;
    font-family: "Didact Gothic", sans-serif;
    font-size: 25px;
    color: var(--ink);
  }
  .card__contact {
    position: absolute;
    left: 91px;
    top: 318px;
    font-family: "Didact Gothic", sans-serif;
    font-size: 27px;
    line-height: 29px;
    color: var(--ink);
    list-style: none;
  }
  .card__studio {
    position: absolute;
    left: 730px;
    top: 454px;
    width: 444px;
    transform: rotate(-90deg);
    transform-origin: 0 0;
    font-family: "Didact Gothic", sans-serif;
    font-size: 44px;
    line-height: 44px;
    letter-spacing: 1px;
    color: var(--studio-green);
    -webkit-text-stroke: 0.8px var(--studio-green);
    text-shadow: 1px 1px 1px var(--studio-edge);
    white-space: nowrap;
  }
  .card__rules {
    position: absolute;
    left: 770px;
    top: 0;
  }
</style>
</head>
<body>
  <section class="card">
    <div class="card__foliage" role="img" aria-label="Abstract camouflage pattern of overlapping green leaf shapes"></div>
    <h1 class="card__name">Lionel Harwicke</h1>
    <p class="card__title">Architect</p>
    <ul class="card__contact">
      <li>NY License No. 052816</li>
      <li>lionel@designlhq.com</li>
      <li>607 382 9154</li>
    </ul>
    <p class="card__studio">Brackenfold Studio</p>
    <svg class="card__rules" width="20" height="461" viewBox="0 0 20 461" aria-hidden="true">
      <line x1="6" y1="0" x2="6" y2="461" stroke="var(--rule-red)" stroke-width="2"/>
      <line x1="17" y1="0" x2="17" y2="461" stroke="var(--rule-red)" stroke-width="2"/>
    </svg>
  </section>
</body>
</html>
```